Need webdesign for service company that provides Car hiring service and transit service

We need a web design for a company that provides airport transit services and transport services including Limo, Corporate cars, Disability transit, Family transit service. We need is a simple and professional design.

Below is site which we like and also offer the same service http://www.ridevelto.com.au/

Reason: Waiting for the Feedback from multiple stakeholders. Need the time to select and approve the design

Target Market(s)

Tourism, Travel

Industry/Entity Type

Airport

Number of Pages Required

3 page

Font styles to use
Decorative
Script

Requirements
Must have
• Simple and Professional, Site we like http://www.ridevelto.com.au/ and also need to mobile friendly
Should not have
• Shouldn't have too many images

```html
<!DOCTYPE html>
<html lang="en">
<head>
<meta charset="utf-8">
<title>Rideway – Private &amp; Business Transport</title>
<link rel="stylesheet" href="https://fonts.googleapis.com/css2?family=Mulish:wght@300;400;600;700&display=swap">
<style>
  :root {
    --ink: #111111;
    --white: #ffffff;
    --taupe: #6f6a6a;
    --muted: #8c8c8c;
    --body: #555555;
    --black: #000000;
    --footer-bg: #f1f1f1;
    --footer-line: #dddddd;
  }
  * { box-sizing: border-box; margin: 0; padding: 0; }
  html, body { width: 1014px; height: 1200px; overflow: hidden; }
  body {
    position: relative;
    background: var(--white);
    font-family: "Mulish", Arial, sans-serif;
    color: var(--ink);
  }

  /* Header */
  .site-header {
    position: absolute; left: 0; top: 0; width: 1014px; height: 84px;
    background: var(--white);
  }
  .brand {
    position: absolute; left: 100px; top: 24px;
    display: flex; align-items: center; gap: 10px;
  }
  .brand-mark { width: 30px; height: 30px; background: var(--ink); }
  .brand-name { font-size: 28px; font-weight: 400; letter-spacing: 0.5px; color: var(--ink); }
  .header-actions {
    position: absolute; right: 104px; top: 28px;
    display: flex; align-items: center; gap: 24px;
  }

  /* Hero */
  .hero {
    position: absolute; left: 0; top: 84px; width: 1014px; height: 503px;
    overflow: hidden;
  }
  .hero-photo {
    position: absolute; inset: 0;
    background: linear-gradient(180deg, #4f5d72 0%, #7a8290 30%, #a7a8aa 55%, #7f7f82 78%, #5d5d60 100%);
  }
  .hero-title {
    position: absolute; left: 0; width: 100%; top: 80px; text-align: center;
    color: var(--white); font-weight: 400; font-size: 50px; letter-spacing: 0.5px; line-height: 1;
  }
  .hero-subtitle {
    position: absolute; left: 0; width: 100%; top: 138px; text-align: center;
    color: var(--white); font-weight: 400; font-size: 22px; line-height: 1;
  }
  .quote-frame {
    position: absolute; left: 304px; top: 235px; width: 406px; height: 183px;
    border: 2px solid rgba(255,255,255,0.7);
  }
  .quote-label {
    position: absolute; left: 387px; top: 218px; width: 240px; height: 36px;
    background: #2f2f30;
    clip-path: polygon(14px 0, calc(100% - 14px) 0, 100% 50%, calc(100% - 14px) 100%, 14px 100%, 0 50%);
    color: var(--white); font-size: 17px; text-align: center; line-height: 36px;
  }
  .quote-field {
    position: absolute; left: 340px; width: 346px; height: 32px;
    background: var(--white); padding-left: 12px;
    font-size: 11.5px; color: #666; line-height: 32px;
  }
  .quote-submit {
    position: absolute; left: 340px; top: 349px; width: 346px; height: 42px;
    background: var(--taupe); color: var(--white);
    font-size: 15px; text-align: center; line-height: 42px;
  }

  /* Service cards */
  .service-card {
    position: absolute; top: 606px; width: 265px; height: 233px;
    background: var(--black); color: var(--white); text-align: center;
  }
  .service-card--alt { background: var(--taupe); }
  .service-icon { position: absolute; left: 0; right: 0; top: 22px; height: 62px; display: flex; justify-content: center; align-items: center; }
  .service-title { position: absolute; left: 0; right: 0; top: 95px; font-size: 16.5px; font-weight: 400; line-height: 19px; }
  .service-text { position: absolute; left: 36px; right: 30px; font-size: 10px; line-height: 14px; color: #b5b0b0; }
  .service-card--alt .service-text { color: #c9c4c4; }
  .read-more-btn {
    position: absolute; left: 50%; transform: translateX(-50%); top: 174px;
    width: 102px; height: 29px; border: 1px solid var(--white);
    font-size: 11px; line-height: 27px; color: var(--white);
  }

  /* News */
  .news-heading { position: absolute; left: 99px; top: 910px; font-size: 23px; font-weight: 400; }
  .news-item { position: absolute; top: 956px; width: 250px; }
  .news-date { font-size: 12px; color: var(--body); }
  .news-title { margin-top: 5px; font-size: 14px; font-weight: 400; color: var(--ink); }
  .news-excerpt { margin-top: 8px; font-size: 10.5px; line-height: 17.5px; color: var(--muted); }
  .news-more { margin-top: 6px; font-size: 10.5px; color: var(--body); }

  /* Footer */
  .site-footer {
    position: absolute; left: 0; top: 1143px; width: 1014px; height: 57px;
    background: var(--footer-bg); border-top: 1px solid var(--footer-line);
    text-align: center; font-size: 12px; color: var(--body); line-height: 24px; padding-top: 11px;
  }
</style>
</head>
<body>

<header class="site-header">
  <div class="brand">
    <span class="brand-mark"></span>
    <span class="brand-name">RIDEWAY</span>
  </div>
  <nav class="header-actions" aria-label="Header actions">
    <svg width="28" height="18" viewBox="0 0 28 18" aria-label="Menu"><rect y="0" width="28" height="3" fill="#111"/><rect y="7.5" width="28" height="3" fill="#111"/><rect y="15" width="28" height="3" fill="#111"/></svg>
    <svg width="20" height="20" viewBox="0 0 24 24" aria-label="Call"><path fill="#8a8a8a" d="M6.6 10.8a15.1 15.1 0 0 0 6.6 6.6l2.2-2.2c.3-.3.7-.4 1-.2 1.1.4 2.3.6 3.6.6.6 0 1 .4 1 1V20c0 .6-.4 1-1 1A17 17 0 0 1 3 4c0-.6.4-1 1-1h3.5c.6 0 1 .4 1 1 0 1.3.2 2.5.6 3.6.1.3 0 .7-.2 1z"/></svg>
    <svg width="20" height="20" viewBox="0 0 24 24" aria-label="Search"><circle cx="10" cy="10" r="7" fill="none" stroke="#8a8a8a" stroke-width="3"/><line x1="15" y1="15" x2="22" y2="22" stroke="#8a8a8a" stroke-width="3.5" stroke-linecap="round"/></svg>
  </nav>
</header>

<section class="hero">
  <div class="hero-photo" role="img" aria-label="White stretch limousine parked in an open car park under a blue sky, darkened overlay"></div>
  <h1 class="hero-title">PRIVATE &amp; BUSINESS</h1>
  <p class="hero-subtitle">PERSONALISED TRANSPORT SERVICES</p>
  <div class="quote-frame"></div>
  <div class="quote-label">GET INSTANT QUOTE</div>
  <div class="quote-field" style="top:275px;">Origin (Public location or Exact address )</div>
  <div class="quote-field" style="top:316px;">Destination (Public location or Exact address )</div>
  <div class="quote-submit">SUBMIT</div>
</section>

<article class="service-card" style="left:99px;">
  <div class="service-icon">
    <svg width="90" height="38" viewBox="0 0 90 38" aria-label="Car icon"><g fill="none" stroke="#fff" stroke-width="2.2" stroke-linejoin="round"><path d="M3 26v-8c0-2 1-3 3-3h12l10-10h30l12 10h12c3 0 5 2 5 5v6H3z"/><path d="M31 8h24v8H27z"/><line x1="41" y1="8" x2="41" y2="16"/><line x1="48" y1="8" x2="48" y2="16"/><circle cx="20" cy="28" r="6" fill="#000"/><circle cx="68" cy="28" r="6" fill="#000"/></g></svg>
  </div>
  <h2 class="service-title">AIRPORT TRANSIT<br>SERVICES</h2>
  <p class="service-text" style="top:142px;">Proin nulla arcu nonummy luctus dictum eget fermentum et lorem</p>
  <span class="read-more-btn">READ MORE</span>
</article>

<article class="service-card service-card--alt" style="left:373px;">
  <div class="service-icon">
    <svg width="46" height="60" viewBox="0 0 46 60" role="img" aria-label="Chauffeur icon"><rect x="3" y="3" width="40" height="54" fill="none" stroke="#fff" stroke-width="2.2"/></svg>
  </div>
  <h2 class="service-title">WHY CHOOSE US</h2>
  <p class="service-text" style="top:124px;">Proin nulla arcu nonummy luctus dictum eget fermentum et lorem Nunc porta convallis pede</p>
  <span class="read-more-btn">READ MORE</span>
</article>

<article class="service-card" style="left:645px;">
  <div class="service-icon">
    <svg width="50" height="50" viewBox="0 0 50 50" aria-label="24 hour support icon"><path d="M14 8a21 21 0 1 1 -2 32" fill="none" stroke="#fff" stroke-width="2.2"/><text x="30" y="23" fill="#fff" font-family="Mulish, sans-serif" font-size="12" font-weight="700" text-anchor="middle">24</text><path d="M8 16l6-4 5 8-4 3c2 5 5 8 10 10l3-4 8 5-4 6c-12-2-22-12-24-24z" fill="none" stroke="#fff" stroke-width="2.2" stroke-linejoin="round"/></svg>
  </div>
  <h2 class="service-title">24/7 SUPPORT</h2>
  <p class="service-text" style="top:122px;">Proin nulla arcu nonummy luctus dictum eget fermentum et lorem Nunc porta convallis pede</p>
  <span class="read-more-btn">READ MORE</span>
</article>

<h2 class="news-heading">NEWS &amp; BLOGS</h2>

<article class="news-item" style="left:101px;">
  <p class="news-date">24 April 2017</p>
  <h3 class="news-title">Sociosqu ad litora torquent</h3>
  <p class="news-excerpt">per conubia nostra per inceptos hymenaeos Proin nulla arcu nonummy luctus dictum eget fermentum et lorem Nunc porta convallis pede</p>
  <p class="news-more">READ MORE</p>
</article>

<article class="news-item" style="left:388px;">
  <p class="news-date">14 April 2017</p>
  <h3 class="news-title">Praesent elementum elit</h3>
  <p class="news-excerpt">per conubia nostra per inceptos hymenaeos Proin nulla arcu nonummy luctus dictum eget fermentum et lorem Nunc porta convallis pede</p>
  <p class="news-more">READ MORE</p>
</article>

<article class="news-item" style="left:687px; width:230px;">
  <p class="news-date">10 April 2017</p>
  <h3 class="news-title">Etiam eleifend metus vitae</h3>
  <p class="news-excerpt">per conubia nostra per inceptos hymenaeos Proin nulla arcu nonummy luctus dictum eget fermentum et lorem Nunc porta convallis pede</p>
  <p class="news-more">READ MORE</p>
</article>

<footer class="site-footer">© 2017 Company Name&nbsp; All right reserved&nbsp; Term of Use</footer>

</body>
</html>
```